Sex Trafficked women Empowered Business Card Design Project

I would like a two-sided business card. On the front, please include: Marta Oberlin, Executive Director 555-284-7316, www.tallowcrest.org, marta@tallowcrest.org and logo.

On the back:
Vision
Survivors of sexual exploitation live free, fulfilling their God-given purpose.

Perhaps a QR code to direct them to the website: www.tallowcrest.org

I want to try a deeper color for the logo. i have added these files.

My desire is to communicate hope, freedom and new life.
Updates

i decided to ask for business card designs with a deeper toned logo. see new files attached

i have placed the vertical logo as an option, but i would still want the logo with tagline used.

Target Market(s)

I want a professional look to appeal to donors who have a heart to help sexually exploited women. I chose a logo that was light enough to look good on a variety of backgrounds. I do want the logo to catch attention.

Industry/Entity Type

Business

Font styles to use
Serif

Requirements
Must have
• i want to be able to read the tagline. Also, the design should match the look and feel of the logo.

Nice to have
• Since there isn't much text on the back, feel free to be a bit more creative. I still want a professional look.

```html
<!DOCTYPE html>
<html lang="en">
<head>
<meta charset="utf-8">
<title>Tallowcrest – Business Card</title>
<link rel="stylesheet" href="https://fonts.googleapis.com/css2?family=Didact+Gothic&family=Tinos&display=swap">
<style>
  :root {
    --paper: #ffffff;
    --ink: #111111;
    --sky: #b4e3f6;
    --sky-deep: #1ba3e0;
    --sun: #fcecb0;
  }
  html, body {
    margin: 0;
    padding: 0;
    overflow: hidden;
    background: var(--paper);
  }
  .card {
    position: relative;
    width: 1200px;
    height: 703px;
    background: var(--paper);
    overflow: hidden;
  }
  .emblem-backdrop {
    position: absolute;
    left: 70px;
    top: 100px;
    width: 520px;
    height: 520px;
    border-radius: 50%;
    background: radial-gradient(circle at 45% 45%, var(--sky) 0%, #d3eefa 55%, var(--sun) 80%, rgba(252,236,176,0) 100%);
    opacity: 0.75;
  }
  .identity {
    position: absolute;
    left: 135px;
    top: 132px;
    font-family: "Didact Gothic", sans-serif;
    color: var(--ink);
  }
  .identity .name {
    margin: 0;
    font-size: 56px;
    font-weight: 400;
    line-height: 1;
    letter-spacing: 0.5px;
  }
  .identity .role {
    margin: 6px 0 0 2px;
    font-size: 25px;
    line-height: 1;
  }
  .contact {
    position: absolute;
    left: 135px;
    top: 453px;
    margin: 0;
    padding: 0;
    list-style: none;
    font-family: "Tinos", serif;
    font-size: 31px;
    line-height: 47px;
    color: var(--ink);
  }
  .brand {
    position: absolute;
    left: 768px;
    top: 80px;
    display: flex;
    align-items: center;
    gap: 14px;
  }
  .brand .mark {
    width: 84px;
    height: 84px;
    border-radius: 50%;
    background: var(--sky-deep);
  }
  .brand .wordmark {
    font-family: "Tinos", serif;
    font-size: 40px;
    color: var(--ink);
    letter-spacing: 0.5px;
  }
</style>
</head>
<body>
  <main class="card">
    <div class="emblem-backdrop" role="img" aria-label="Large faint bird emblem in light blue inside a pale yellow ring"></div>

    <header class="identity">
      <h1 class="name">Marta Oberlin</h1>
      <p class="role">Executive Director</p>
    </header>

    <ul class="contact">
      <li>555-284-7316</li>
      <li>www.tallowcrest.org</li>
      <li>marta@tallowcrest.org</li>
    </ul>

    <div class="brand">
      <span class="mark"></span>
      <span class="wordmark">Tallowcrest</span>
    </div>
  </main>
</body>
</html>
```